Town Wordpress Design Project

Hi,
I am looking for someone to completely start from scratch on a website for a town in Texas named Lakeside. I designed their last website about 4 years ago but am not able to give them what I would like to with my abilities. I need a wordpress website that is web 2.0 in design while still being creative. Their current website can be seen at www.marbleforkvale.us. They like such websites by a company named MuniBolt, you can view their town website portfolio here: http://www.munibolt.com/index.aspx?NID=137. I would need all of the pages and info that is on their current site to be moved to the new site that I am hoping you can create for me. I want a much cleaner, nicer, and simpler navigation panel, while hiding links in drop down menus. I also want to include a calendar where they could post upcoming events and would want them to be able to add submit-able forms whenever they would need to. A search option would also be nice. I know that this is a design community, but if you could code the site as well or know someone who can, please let me know. Their Town Logo can be found attached, and the font in which you spell out their town name is totally up to you. They want their Agenda and Minutes to display like this: http://www.qdvwb.com/index.aspx?NID=266. Let me know if you have any further questions...
If at all possible, I wouldn't mind the design to be designed in such a way that making it "responsive" someday would be easily possible...
Reason: More time needed for some designers...
Reason: Additional time needed...

```html
<!DOCTYPE html>
<html lang="en">
<head>
<meta charset="utf-8">
<title>Lakeside – Town Home</title>
<link href="https://fonts.googleapis.com/css2?family=Source+Sans+3:wght@400;600;700&family=Arimo:wght@400;700&display=swap" rel="stylesheet">
<style>
:root{
  --page:#f3f2ea;
  --side:#ebebe9;
  --line:#d6d5cd;
  --grey-head:#6c6c6c;
  --blue:#3fb0e6;
  --blue-dark:#2a7fc4;
  --green:#55b73b;
  --date:#b3b3b3;
  --body:#555;
  --ink:#222;
  --maroon:#5a2733;
  --cal-dark:#1d1d1d;
}
*{box-sizing:border-box;margin:0;padding:0}
html,body{width:1200px;height:1157px;overflow:hidden}
body{background:var(--page);font-family:"Source Sans 3",sans-serif;color:var(--ink);position:relative}
.side-panel{position:absolute;left:711px;top:0;width:412px;height:1147px;background:var(--side);border-left:1px solid var(--line);border-right:1px solid var(--line)}
.section-title{position:absolute;font-size:35px;font-weight:700;color:var(--grey-head);letter-spacing:.2px;white-space:nowrap}
.section-title .hl{color:var(--blue)}
.news{position:absolute;left:113px;width:560px;height:229px}
.news h3{font-size:24px;font-weight:700;color:var(--green);margin-left:6px;line-height:1.1}
.news .when{font-size:19px;font-weight:700;color:var(--date);margin-left:6px;line-height:1.2}
.news p{font-family:"Arimo",sans-serif;font-size:14.6px;line-height:18px;color:var(--body);margin:18px 0 0 6px;width:536px;text-indent:56px}
.news .more{font-size:17px;color:var(--ink);margin:9px 0 0 6px}
.view-more{position:absolute;left:257px;top:812px;width:226px;height:32px;background:var(--blue);color:#fff;font-weight:700;font-size:17px;display:flex;align-items:center;justify-content:space-between;padding:0 10px}
.view-more i{font-style:normal;font-weight:400;opacity:.9}
.rule{position:absolute;height:1px;background:var(--line)}
.calendar{position:absolute;left:751px;top:89px;width:336px;height:244px;background:var(--cal-dark);border-radius:3px;padding:0 10px}
.cal-head{height:36px;display:flex;align-items:center;justify-content:space-between;color:#fff;font-family:"Arimo",sans-serif;font-weight:700;font-size:13px}
.cal-head span{width:20px;height:20px;border-radius:50%;background:#3a3a3a;border:1px solid #555;display:flex;align-items:center;justify-content:center;font-size:9px}
.cal-grid{display:grid;grid-template-columns:repeat(7,1fr);gap:2px;background:#9b9b9b;border:1px solid #9b9b9b}
.cal-grid b,.cal-grid em{height:26px;display:flex;align-items:center;justify-content:center;font-family:"Arimo",sans-serif;font-size:12px;font-weight:700;color:#222;background:linear-gradient(#f2f2f2,#d9d9d9);position:relative}
.cal-grid em{font-style:italic;font-weight:400;font-size:11.5px;height:20px;background:linear-gradient(#e8e8e8,#cfcfcf);color:#333}
.cal-grid .muted{color:#aaa}
.cal-grid .today{background:linear-gradient(#5ab3ef,#2a86d6);color:#fff}
.cal-grid .has-event::after{content:"";position:absolute;top:3px;right:8px;width:5px;height:5px;border-radius:50%;background:var(--blue-dark)}
.events{position:absolute;left:751px;top:333px;width:336px;height:475px;border:2px solid #cfcfcf;border-top:none;border-radius:0 0 6px 6px;background:var(--page);overflow:hidden}
.events .day{text-align:center;color:var(--blue);font-weight:700;font-size:16px;margin-top:6px;margin-right:24px}
.events .day-rule{height:4px;border-top:1px solid #bbb;border-bottom:1px solid #bbb;margin:3px 40px 0 28px}
.scroll{position:absolute;right:4px;top:0;width:16px;height:473px;border-left:1px solid #d0d0d0;background:#efefea}
.scroll span{position:absolute;left:2px;top:167px;width:12px;height:67px;background:#b9b9b5;border-radius:6px}
.event{position:absolute;left:20px;width:288px;height:136px;border-bottom:1px solid #cfcfcf}
.event h4{font-size:20px;font-weight:600;color:var(--maroon)}
.event .thumb{position:absolute;left:-2px;top:34px;width:56px;height:56px;border-radius:50%;background:radial-gradient(circle at 40% 40%,#4aa4ea,#1f6fc8)}
.event .teaser{position:absolute;left:63px;top:43px;font-family:"Arimo",sans-serif;font-weight:700;font-size:12.5px;line-height:17px;color:var(--blue-dark)}
.event .teaser sup{font-size:8px}
.event .share{position:absolute;left:50px;top:96px;display:flex;align-items:center;gap:4px;font-family:"Arimo",sans-serif;font-size:8.5px;color:#888}
.event .share strong{color:var(--blue-dark);font-size:8.5px;margin-right:2px}
.event .share i{width:9px;height:9px;border-radius:50%;background:var(--blue-dark);display:inline-block}
.event .share i.red{background:#d43b3b}
.event .share small{margin-left:12px;font-size:8.5px}
.foot-title{position:absolute;font-size:34px;font-weight:600;color:var(--blue);white-space:nowrap}
.foot-title .dim{color:var(--grey-head)}
.dotted{position:absolute;height:0;border-top:1px dotted #bdbdb5}
.foot-copy{position:absolute;font-size:14.5px;line-height:15px;color:#222}
.social{position:absolute;top:997px;left:89px;display:flex;gap:8px}
.social span{width:64px;height:64px;border-radius:50%;background:#fff;box-shadow:0 2px 4px rgba(0,0,0,.3);display:flex;align-items:center;justify-content:center}
.social span b{width:52px;height:52px;border-radius:50%;background:var(--blue-dark);color:#fff;font-size:12px;font-weight:600;display:flex;align-items:center;justify-content:center}
.email-field{position:absolute;left:395px;top:992px;width:294px;height:31px;border:1px solid #d0d0d0;background:#fff;font-family:"Arimo",sans-serif;font-size:11px;color:#c5c5c5;padding:8px 10px}
.subscribe{position:absolute;left:395px;top:1036px;width:162px;height:31px;border-radius:3px;background:linear-gradient(#3f7ec0,#1d4f8e);color:#fff;font-family:Georgia,serif;font-size:13px;display:flex;align-items:center;justify-content:space-between;padding:0 10px}
.contact{position:absolute;left:768px;font-size:15px;color:#222}
.contact b{display:inline-block;width:64px;font-size:17px;font-weight:700}
.strip{position:absolute;left:0;bottom:0;width:1200px;height:10px;background:linear-gradient(90deg,#e34a3b 0 9%,#f2a31f 9% 17%,#5bb84a 17% 27%,#3ba6e3 27% 36%,#e34a3b 36% 44%,#f5c62a 44% 53%,#5bb84a 53% 62%,#3ba6e3 62% 71%,#e34a3b 71% 79%,#f2a31f 79% 88%,#5bb84a 88% 94%,#3ba6e3 94% 100%)}
</style>
</head>
<body>
<div class="side-panel"></div>

<h1 class="section-title" style="left:89px;top:34px">What happening in <span class="hl">LAKESIDE?</span></h1>

<article class="news" style="top:98px">
  <h3>Safe Street Night Event in Lakeside</h3>
  <div class="when">on Tuesday, October 2nd.</div>
  <p>Please reserve this date on your calendar! Come out and participate in a Safe Street Night event at Town Hall on Tuesday, October 2nd. This event will be held in participation with the Hollin County Sheriff's Department and include surrounding communities. Safe Street Night is designed to heighten crime and drug prevention awareness; generate support for, and participation in, Local anti-crime programs.</p>
  <div class="more">More details to follow in the coming weeks.</div>
</article>
<div class="rule" style="left:113px;top:327px;width:560px"></div>
<article class="news" style="top:336px">
  <h3>Safe Street Night Event in Lakeside</h3>
  <div class="when">on Tuesday, October 2nd.</div>
  <p>Please reserve this date on your calendar! Come out and participate in a Safe Street Night event at Town Hall on Tuesday, October 2nd. This event will be held in participation with the Hollin County Sheriff's Department and include surrounding communities. Safe Street Night is designed to heighten crime and drug prevention awareness; generate support for, and participation in, Local anti-crime programs.</p>
  <div class="more">More details to follow in the coming weeks.</div>
</article>
<div class="rule" style="left:113px;top:564px;width:560px"></div>
<article class="news" style="top:573px">
  <h3>Safe Street Night Event in Lakeside</h3>
  <div class="when">on Tuesday, October 2nd.</div>
  <p>Please reserve this date on your calendar! Come out and participate in a Safe Street Night event at Town Hall on Tuesday, October 2nd. This event will be held in participation with the Hollin County Sheriff's Department and include surrounding communities. Safe Street Night is designed to heighten crime and drug prevention awareness; generate support for, and participation in, Local anti-crime programs.</p>
  <div class="more">More details to follow in the coming weeks.</div>
</article>

<div class="view-more"><i>||</i>View More<i>||</i></div>
<div class="rule" style="left:103px;top:845px;width:561px"></div>

<h2 class="section-title" style="left:748px;top:34px">Upcoming <span class="hl">EVENTS</span></h2>

<div class="calendar">
  <div class="cal-head"><span>&#9664;</span>September, 2012<span>&#9654;</span></div>
  <div class="cal-grid">
    <em>Sun</em><em>Mon</em><em>Tue</em><em>Wed</em><em>Thu</em><em>Fri</em><em>Sat</em>
    <b class="muted">27</b><b class="muted">28</b><b>1</b><b>2</b><b>3</b><b>4</b><b>5</b>
    <b>6</b><b>7</b><b>8</b><b class="has-event">9</b><b>10</b><b>11</b><b>12</b>
    <b>13</b><b>14</b><b>15</b><b>16</b><b>17</b><b class="today">18</b><b>19</b>
    <b>20</b><b>21</b><b class="has-event">22</b><b>23</b><b>24</b><b>25</b><b>26</b>
    <b>27</b><b>28</b><b>29</b><b>30</b><b>31</b><b class="muted">1</b><b class="muted">2</b>
    <b class="muted">3</b><b class="muted">4</b><b class="muted">5</b><b class="muted">6</b><b class="muted">7</b><b class="muted">8</b><b class="muted">9</b>
  </div>
</div>

<section class="events">
  <div class="day">On Friday, 18 Sep, 2012</div>
  <div class="day-rule"></div>
  <div class="scroll"><span></span></div>
  <div class="event" style="top:50px">
    <h4>Water Conservation Plan</h4>
    <div class="thumb" role="img" aria-label="Water conservation illustration"></div>
    <div class="teaser">WATER CONSERVATION PLAN<br>BEGINS MAY 1<sup>ST</sup>. Click for Details.</div>
    <div class="share"><strong>Share On</strong><i></i><i></i><i></i><i class="red"></i><small>On Tuesday, 6 Sep, 2012</small></div>
  </div>
  <div class="event" style="top:186px">
    <h4>Water Conservation Plan</h4>
    <div class="thumb" role="img" aria-label="Water conservation illustration"></div>
    <div class="teaser">WATER CONSERVATION PLAN<br>BEGINS MAY 1<sup>ST</sup>. Click for Details.</div>
    <div class="share"><strong>Share On</strong><i></i><i></i><i></i><i class="red"></i><small>On Tuesday, 6 Sep, 2012</small></div>
  </div>
  <div class="event" style="top:322px;border-bottom:none">
    <h4>Water Conservation Plan</h4>
    <div class="thumb" role="img" aria-label="Water conservation illustration"></div>
    <div class="teaser">WATER CONSERVATION PLAN<br>BEGINS MAY 1<sup>ST</sup>. Click for Details.</div>
    <div class="share"><strong>Share On</strong><i></i><i></i><i></i><i class="red"></i><small>On Tuesday, 6 Sep, 2012</small></div>
  </div>
</section>
<div class="rule" style="left:721px;top:845px;width:375px"></div>

<h2 class="foot-title" style="left:84px;top:877px">Follow Us <span class="dim">On</span></h2>
<div class="dotted" style="left:84px;top:921px;width:287px"></div>
<p class="foot-copy" style="left:115px;top:931px;width:255px">At vero eos et accusamuset iusto odio dssimos ducimus qui blanditiis praesentium</p>
<div class="social">
  <span><b>Kivo</b></span><span><b>Palnet</b></span><span><b>Workly</b></span><span><b>Circlo</b></span>
</div>

<h2 class="foot-title" style="left:388px;top:877px">Newsletter</h2>
<div class="dotted" style="left:388px;top:921px;width:296px"></div>
<p class="foot-copy" style="left:423px;top:931px;width:255px">At vero eos et accusamuset iusto odio dssimos ducimus qui blanditiis praesentium</p>
<div class="email-field">your email address</div>
<div class="subscribe">Subscribe<span>&#10230;</span></div>

<h2 class="foot-title" style="left:748px;top:877px">Contact Us <span class="dim">On</span></h2>
<div class="dotted" style="left:748px;top:921px;width:294px"></div>
<div class="contact" style="top:930px"><b>Email:-</b>Contact@postvale.com</div>
<div class="contact" style="top:966px"><b>Site:-</b>Website: www.Bizvale.com</div>
<div class="contact" style="top:1002px"><b>Phone:-</b>Phone: 214-555-0187</div>

<div class="strip"></div>
</body>
</html>
```